Single brochure for international companies in the financial sector

We need to update a brochure 4 pages presenting our company. We are a financial engineering company. The final design must provide financial security, service and trust. you will find the current brochure copy. Our color code is Orange (RGB 235/100/68), Black, White and Gray. photos show the visual of the site, but it is not mandatory to keep them.

Target Market(s)

wealth management professionals

Industry/Entity Type

Finance

Requirements
Must have
• Logo Tolvane Capital all text in the document color Orange Tolvane (RGB 235/100/68)
Nice to have
• Vista Font
Should not have
• images / pictures of people

```html
<!DOCTYPE html>
<html lang="en">
<head>
<meta charset="utf-8">
<title>Tolvane Capital – Brochure Spreads</title>
<link rel="stylesheet" href="https://fonts.googleapis.com/css2?family=Raleway:wght@300;400;500&family=Roboto+Condensed:wght@700&display=swap">
<style>
  :root {
    --board: #58595b;
    --orange: #eb6444;
    --orange-deep: #d8432c;
    --orange-light: #f07553;
    --ink: #1d1d1d;
    --white: #ffffff;
    --paper: #fbf8f8;
    --gray-light: #e4e4e4;
    --gray-mid: #a9a9a9;
  }
  * { margin: 0; padding: 0; box-sizing: border-box; }
  html, body { width: 836px; height: 1200px; overflow: hidden; background: var(--board); }
  body { position: relative; font-family: "Raleway", Arial, sans-serif; color: var(--white); }

  .page-label {
    position: absolute; font-family: "Roboto Condensed", Arial, sans-serif;
    font-weight: 700; font-size: 18px; color: var(--white);
  }

  .panel { position: absolute; overflow: hidden; box-shadow: 0 1px 3px rgba(0,0,0,.35); }
  .panel--orange {
    background: linear-gradient(100deg, var(--orange-deep) 0%, var(--orange) 45%, var(--orange-light) 70%, var(--orange-deep) 100%);
  }
  .panel--paper {
    background: radial-gradient(ellipse at 60% 40%, #ffffff 0%, var(--paper) 55%, #f5ecec 100%);
  }

  .abs { position: absolute; }

  /* wordmark */
  .wordmark { position: absolute; text-align: center; font-weight: 400; text-transform: uppercase; }
  .wordmark span { display: block; }

  /* back cover */
  .legal { position: absolute; left: 39px; width: 382px; text-align: center; font-size: 8px; letter-spacing: .5px; line-height: 10px; color: rgba(255,255,255,.85); }

  /* inner spread */
  .section-title { position: absolute; font-weight: 300; font-size: 19px; letter-spacing: 1.5px; text-transform: uppercase; }
  .heading { position: absolute; font-weight: 400; font-size: 12px; text-transform: uppercase; }
  .copy { position: absolute; font-weight: 300; font-size: 7.3px; line-height: 11px; text-align: justify; color: rgba(255,255,255,.92); }
  .copy p + p { margin-top: 6px; }

  .photo-strip { position: absolute; left: 234px; top: 646px; width: 168px; height: 456px; background: linear-gradient(90deg, #d6d6d6, #f4f4f4 50%, #d8d8d8); }
  .quote { position: absolute; left: 244px; top: 838px; width: 148px; text-align: center; font-weight: 300; font-size: 8.4px; line-height: 13px; color: #3a3a3a; text-transform: uppercase; }
  .quote p + p { margin-top: 7px; }

  .perks { position: absolute; left: 430px; top: 842px; list-style: none; }
  .perks li { display: flex; align-items: center; height: 18.6px; font-size: 6.6px; font-weight: 400; text-transform: uppercase; }
  .perks svg { margin-right: 4px; }

  .promo-card { position: absolute; left: 448px; top: 950px; width: 324px; height: 168px; border-radius: 9px; background: radial-gradient(ellipse at 50% 45%, #ffffff 0%, #f1f1f1 55%, #cfcfcf 100%); }
</style>
</head>
<body>

<div class="page-label" style="left:44px; top:12px;">Page 4</div>
<div class="page-label" style="left:748px; top:15px;">Page 1</div>
<div class="page-label" style="left:40px; top:1160px;">Page 2</div>
<div class="page-label" style="left:744px; top:1163px;">Page 3</div>

<!-- Back cover (page 4) -->
<section class="panel panel--orange" style="left:39px; top:47px; width:382px; height:541px;">
  <div class="wordmark" style="left:0; width:382px; top:298px; color:var(--ink);">
    <span style="font-size:20px; letter-spacing:12px; padding-left:12px;">Tolvane</span>
    <span style="font-size:14px; letter-spacing:6px; padding-left:6px; margin-top:8px;">Capital</span>
  </div>
</section>
<div class="legal" style="top:482px;">Tolvane Capital SA.<br>Capital : 400 000 Euros</div>
<div class="legal" style="top:508px;">RCS Paris : 812 447 905</div>
<div class="legal" style="top:525px;">Code Banque (CIB) : 14726</div>
<div class="legal" style="top:552px; letter-spacing:1.8px;">www.tolvanecapital.com</div>

<!-- Front cover (page 1) -->
<section class="panel panel--paper" style="left:421px; top:47px; width:381px; height:541px;">
  <div class="wordmark" style="left:0; width:381px; top:116px; color:var(--ink);">
    <span style="font-size:34px; letter-spacing:20px; padding-left:20px;">Tolvane</span>
    <span style="font-size:24px; letter-spacing:9px; padding-left:9px; margin-top:10px;">Capital</span>
  </div>
  <div class="abs" role="img" aria-label="Line sketch of a modern multi-storey office building"
       style="left:80px; top:329px; width:220px; height:144px; background:linear-gradient(180deg, rgba(60,60,60,.05), rgba(60,60,60,.18));"></div>
  <div class="abs" style="left:0; width:381px; top:483px; text-align:center; font-weight:300; font-size:19px; color:var(--orange);">FINANCIAL ENGINEERING</div>
</section>

<!-- Inner spread (pages 2–3) -->
<section class="panel panel--orange" style="left:39px; top:611px; width:763px; height:541px;"></section>

<h2 class="section-title" style="left:56px; top:643px;">The Company</h2>

<h3 class="heading" style="left:56px; top:707px;">About us</h3>
<div class="copy" style="left:56px; top:734px; width:162px;">
  <p>Tolvane Capital is a financial engineering company.</p>
  <p>It is fully independent from any bank or any other company.</p>
</div>

<h3 class="heading" style="left:56px; top:835px;">Our clients</h3>
<div class="copy" style="left:56px; top:862px; width:162px;">
  <p>Our clients are financial professionals such as asset managers, institutionnals, corporates, private banks, wealth managers and family offices.</p>
  <p>Our purpose is to make their work easier, every day.</p>
</div>

<h3 class="heading" style="left:56px; top:985px;">What we do</h3>
<div class="copy" style="left:56px; top:1012px; width:162px;">
  <p>We provide them with investment solutions designed to improve their portfolios performance.</p>
  <p>Simple as that.</p>
</div>

<div class="photo-strip">
  <div class="abs" role="img" aria-label="Black and white photo of cobblestone street with tram rails"
       style="left:7px; top:7px; width:153px; height:176px; background:linear-gradient(160deg, #8a8a8a, #4a4a4a 60%, #2e2e2e);"></div>
  <div class="abs" role="img" aria-label="Black and white photo of a stone bridge arch seen from below"
       style="left:7px; top:288px; width:153px; height:160px; background:linear-gradient(135deg, #f2f2f2 30%, #777 55%, #2a2a2a 100%);"></div>
</div>
<div class="quote">
  <p>“Our clients must deliver performance on their portfolios on a regular basis.</p>
  <p>We help them deliver everyday.”</p>
</div>

<h2 class="section-title" style="left:421px; width:381px; text-align:center; top:643px;">Our Services</h2>

<h3 class="heading" style="left:430px; top:711px;">Investment advice</h3>
<div class="copy" style="left:430px; top:738px; width:162px;">
  <p>Each client is looking for a unique investment solution. Hence, we combine internal and external resources to create the financial product that will best fit our clients requirements.</p>
  <p>Thanks to a truly independent advice, we offer bespoke, simple and efficient solutions.</p>
</div>

<ul class="perks">
  <li><svg width="14" height="14" viewBox="0 0 14 14"><circle cx="7" cy="7" r="6.3" fill="none" stroke="#fff" stroke-width=".9"/></svg>A taylormade advice</li>
  <li><svg width="14" height="14" viewBox="0 0 14 14"><circle cx="7" cy="7" r="6.3" fill="none" stroke="#fff" stroke-width=".9"/></svg>An objective advice</li>
  <li><svg width="14" height="14" viewBox="0 0 14 14"><circle cx="7" cy="7" r="6.3" fill="none" stroke="#fff" stroke-width=".9"/></svg>A clear advice</li>
  <li><svg width="14" height="14" viewBox="0 0 14 14"><circle cx="7" cy="7" r="6.3" fill="none" stroke="#fff" stroke-width=".9"/></svg>An advice which gives you the choice</li>
  <li><svg width="14" height="14" viewBox="0 0 14 14"><circle cx="7" cy="7" r="6.3" fill="none" stroke="#fff" stroke-width=".9"/></svg>A long term follow-up</li>
</ul>

<h3 class="heading" style="left:615px; top:711px;">Portfolio analysis</h3>
<div class="copy" style="left:615px; top:738px; width:165px;">
  <p>We advise our clients on their portfolios of financial products. Together we identify the needs for restructuring or reallocating the assets.</p>
  <p>We also provide full monitoring and reporting services throughout the life of the products.</p>
</div>

<h3 class="heading" style="left:615px; top:840px;">Partner selection</h3>
<div class="copy" style="left:615px; top:867px; width:165px;">
  <p>Our internal tools allow us to continuously assess the issuers we are working with.</p>
  <p>Therefore we give our clientsthe luxury to chose among the best issuers for their investment solution.</p>
</div>

<div class="promo-card">
  <div class="wordmark" style="left:0; width:324px; top:28px; color:var(--ink);">
    <span style="font-size:13px; letter-spacing:8px; padding-left:8px;">Tolvane</span>
    <span style="font-size:10px; letter-spacing:4px; padding-left:4px; margin-top:5px;">Capital</span>
  </div>
  <div class="abs" role="img" aria-label="Line sketch of a modern multi-storey office building"
       style="left:80px; top:66px; width:160px; height:102px; background:linear-gradient(180deg, rgba(60,60,60,.06), rgba(60,60,60,.2));"></div>
</div>

</body>
</html>
```